Custom Business Card Design

We are looking for a raised spot logo design to use with Tavu.com. We will provide the logo files. Should be a front and back design. We want to implement the house into the back design using the same colors as the logo through out. Something VERY cool!

```html
<!DOCTYPE html>
<html lang="en">
<head>
<meta charset="utf-8">
<title>Tavu Business Card – Front and Back</title>
<link href="https://fonts.googleapis.com/css2?family=Arimo:wght@400;700&display=swap" rel="stylesheet">
<style>
  :root {
    --brand-blue: #2f74b5;
    --brand-red: #e0383e;
    --ink-grey: #555a60;
    --rule-grey: #8a8d91;
    --card-white: #f7f7f7;
    --backdrop: #e7e4df;
  }
  * { box-sizing: border-box; margin: 0; padding: 0; }
  html, body {
    width: 1200px;
    height: 1023px;
    overflow: hidden;
    background: var(--backdrop);
    font-family: "Arimo", Arial, sans-serif;
  }
  .sheet {
    width: 1200px;
    height: 1023px;
    display: flex;
    flex-direction: column;
    align-items: center;
    justify-content: center;
    gap: 70px;
  }
  .card {
    width: 630px;
    height: 360px;
    background: var(--card-white);
    box-shadow: 0 2px 6px rgba(0,0,0,.18);
    position: relative;
  }

  /* Brand lockup */
  .brand {
    display: flex;
    align-items: center;
    gap: 14px;
  }
  .brand-dot {
    width: 46px;
    height: 46px;
    border-radius: 50%;
    background: var(--brand-blue);
    flex: none;
  }
  .brand-name {
    font-weight: 700;
    font-size: 54px;
    color: var(--brand-blue);
    letter-spacing: 1px;
    line-height: 1;
  }

  /* Front */
  .card-front {
    display: flex;
    align-items: center;
    padding: 0 48px;
  }
  .front-brand { width: 290px; }
  .front-brand .brand-name { font-size: 48px; }
  .front-brand .brand-dot { width: 38px; height: 38px; }
  .divider {
    width: 1.5px;
    height: 170px;
    background: var(--rule-grey);
    margin: 0 34px 0 10px;
  }
  .contact-block { color: var(--ink-grey); }
  .person-name {
    font-weight: 700;
    font-size: 20px;
    color: var(--brand-blue);
  }
  .person-role {
    font-size: 14px;
    color: var(--brand-red);
    margin: 2px 0 18px;
  }
  .contact-list { list-style: none; font-size: 13px; }
  .contact-list li {
    display: flex;
    align-items: center;
    gap: 8px;
    margin-bottom: 5px;
  }
  .contact-icon { width: 14px; height: 14px; flex: none; }
  .address {
    font-size: 13px;
    margin-top: 18px;
    line-height: 1.35;
  }

  /* Back */
  .card-back {
    display: flex;
    align-items: center;
    justify-content: center;
  }
  .back-brand .brand-name { font-size: 84px; }
  .back-brand .brand-dot { width: 70px; height: 70px; }
</style>
</head>
<body>
<main class="sheet">

  <section class="card card-front" aria-label="Card front">
    <div class="brand front-brand">
      <span class="brand-dot"></span>
      <span class="brand-name">Tavu</span>
    </div>
    <div class="divider"></div>
    <div class="contact-block">
      <p class="person-name">Dana Reyes</p>
      <p class="person-role">Founder</p>
      <ul class="contact-list">
        <li>
          <svg class="contact-icon" viewBox="0 0 14 14"><circle cx="7" cy="7" r="7" fill="var(--brand-blue)"/><path d="M4.5 3.5l1.5 0 .6 1.8-.9.7a5 5 0 0 0 2.3 2.3l.7-.9 1.8.6v1.5c-3.6.3-6.3-2.4-6-6z" fill="#fff"/></svg>
          +555 01 2468
        </li>
        <li>
          <svg class="contact-icon" viewBox="0 0 14 14"><circle cx="7" cy="7" r="7" fill="var(--brand-blue)"/><rect x="4" y="5.5" width="6" height="4" fill="#fff"/><rect x="5" y="3.5" width="4" height="2" fill="#fff"/></svg>
          +555 013 579
        </li>
        <li>
          <svg class="contact-icon" viewBox="0 0 14 14"><circle cx="7" cy="7" r="7" fill="var(--brand-blue)"/><rect x="3.5" y="4.5" width="7" height="5" fill="#fff"/><path d="M3.5 4.5l3.5 3 3.5-3" stroke="var(--brand-blue)" stroke-width=".8" fill="none"/></svg>
          info@tavu.com
        </li>
        <li>
          <svg class="contact-icon" viewBox="0 0 14 14"><circle cx="7" cy="7" r="7" fill="var(--brand-blue)"/><circle cx="7" cy="7" r="3.6" fill="none" stroke="#fff" stroke-width=".9"/><path d="M3.4 7h7.2M7 3.4v7.2" stroke="#fff" stroke-width=".8"/></svg>
          www.tavu.com
        </li>
      </ul>
      <p class="address">Here your company or<br>home address</p>
    </div>
  </section>

  <section class="card card-back" aria-label="Card back">
    <div class="brand back-brand">
      <span class="brand-dot"></span>
      <span class="brand-name">Tavu</span>
    </div>
  </section>

</main>
</body>
</html>
```